Interactive Children's Media Book Company Website Design

We need a website DESIGN (no coding required) for a new interactive children's media book company called Tovira Studios.

We develop high-quality interactive children's books for the iPad/iPhone that seeks to delight and inspire young and old alike. Our stories are filled with heart and spirit, and we seek to breathe magic back into books so that people fall back in love with reading.

Tovira means "butterfly" in Korean. It plays on the idea that a caterpillar metamorphoses into a butterfly - and in the same way, our readers are transformed through the journey of experiencing our interactive books.

We're looking for something based on the ATTACHED LOGO DESIGN for our company. A website that's professional, modern, fun and inviting; easy to read and not-cluttered, but still portraying the feeling of innocence and childhood.

We're looking for something that resonates the magical experience we want to create for our readers. Specific requirements on pages, tabs, content, etc are below.

Industry/Entity Type

It Company

Requirements
Nice to have
• There are 7 tabs on the Homepage of the website: HOME, GRANDPA, ABOUT US, CAREERS, NEWS, CONTACT US, SHOP. (But there is an extra page called THEIR GARDEN, which will be a sub-page under Grandpa).

HOME
• Would be great to have some key images of our book (3-4 screen shots) as the key focus of the homepage that automatically scroll through every few seconds. (Placeholder image attached). The images would link to the “Grandpa” page.
• Company logo (attached to brief) and slogan: “A new era of children’s media” quite prominent on page.
• Key text content to be on page: “Tovira means “butterfly” in Korean. Just as a caterpillar transforms into a butterfly, Tovira Studios takes the reader on an unforgettable journey of metamorphosis through our stories. We turn children’s books into a high-quality interactive experience on mobile platforms - breathing magic back into books, and inspiring people to fall back in love with reading. Through our unique characters full of heart and spirit, our stories delight and inspire young and old alike.”
• Chirpline & Facelinks Like & Facelinks page link icons.
• Section on Latest News with a few of the latest entries.
• Section on latest sister images & comments that visitors have posted, which takes you to the “Their Garden” page.

GRANDPA
• The title for this page is “Grandpa Keeps a Secret Garden”
• There will be a little iPad/iPhone icon (placeholder attached) for this book.
• There will be a link to the App Store to buy the app book.
• Key text content on this page: “Our debut interactive media book is coming soon on the iPad and iPhone! “Grandpa Keeps a Secret Garden” touches on the beautiful and inextricable (albeit sometimes frustrating!) bond between sisters.”
• There will be a section on “Features” which lists all the various special features the app book includes.
• There will be a YouTube clip embedded into the page, which shows how the app book works.
• A section that says: “Do you have a sister who’s not like other sisters? Share a photo and tell us about her!” which links to the sub-page “Their Garden”.
• Under this, there may be the most recent few images submitted by the public, which when clicked on, would also link to the sub-page “Their Garden”.

THEIR GARDEN
• The main text on the page: “Do you have a sister who’s not like other sisters? Share a photo and tell us about her!”
• Main body of the page is a gallery of all the photos that have been submitted. If you click on each of the images, you get the comments that people have submitted with the photos.
• The page would also have a Submit Comments Form, where people can upload a picture of their sister(s) and write a comment to accompany the image.

ABOUT US
• Introductory text on page: “It was a chance conversation at Harbourview Terminal, where two friends discovered they shared a dream to create quality children's media. Both of them were excited by the possibilities of using new digital platforms to inspire and educate a younger generation. From that idea Tovira Studios was born. We seek to be the chrysalis of story telling - to inspire the hearts and minds of our generation, and generations to come.”
• Section to “Join the Mailing List” where they can put their email address in and submit.
• Bios of 2x people with photos (bios in word doc attached) (do not have photos yet).

CAREERS
• The main text on the page: “We are always on the lookout for talented people to join our team. If you are a writer, illustrator, animator, iOS/android developer, musician, creative-writing translator - or have something special to offer Tovira Studios - we are keen to hear from you. Send us a message through the Contact Us tab above.”

NEWS
• Regular News page, with blog-type entries.

CONTACT US
• Online submit Contact Us form
• The main text on page: “Our studio is based in the Marram Arts Hub, 14 Pellham Street, Ardlow, Wellington. Marram is a professional, creative collective - with four separate studios, gallery, and retail store. For more information on Marram, visit: http://www.marramhub.example.nz”
• “We would love to hear from you! Whether you have questions, ideas, comments, or just want to say hullo - please leave us a message and we will get back to you soon.”
• Including image of the premises (Marram image attached to brief).

SHOP
• Where visitors can purchase merchandise (t-shirts, mugs, etc) of the book/company.

```html
<!DOCTYPE html>
<html lang="en">
<head>
<meta charset="utf-8">
<title>Tovira Studios – A new era of children’s media</title>
<link rel="stylesheet" href="https://fonts.googleapis.com/css2?family=Arvo:wght@400;700&family=Lora:ital,wght@0,400;0,700;1,400;1,700&family=Arimo:wght@400;700&display=swap">
<style>
  :root{
    --sky-top:#2f8fdc;
    --sky-mid:#7cc3f0;
    --sky-low:#cfe9f9;
    --page-pale:#e9f6fd;
    --white:#ffffff;
    --ink:#555a60;
    --ink-soft:#6b7077;
    --accent-blue:#3a5fcf;
    --follow-blue:#2764b5;
    --tab-home:#f7941d;
    --tab-grandpa:#f9c21a;
    --tab-about:#f26522;
    --tab-careers:#ec4f9c;
    --tab-news:#8e5ec9;
    --tab-contact:#5cc6a0;
    --tab-shop:#8fd3f5;
    --leaf-dark:#1f8a2c;
    --leaf-light:#8fd14f;
    --footer-brown:#5a3b26;
    --night:#000000;
  }
  *{box-sizing:border-box;margin:0;padding:0}
  html,body{width:1200px;height:900px;overflow:hidden;background:var(--night)}
  .canvas{position:relative;width:1200px;height:900px;overflow:hidden;background:var(--night)}
  .page{position:absolute;left:0;top:0;width:1200px;height:764px;
    background:linear-gradient(180deg,var(--sky-top) 0,var(--sky-mid) 150px,var(--sky-low) 300px,var(--page-pale) 620px,var(--page-pale) 764px)}

  .brand{position:absolute;left:18px;top:70px;display:flex;align-items:center;gap:12px}
  .brand-dot{width:44px;height:44px;border-radius:50%;background:#b9a3e8}
  .brand-name{font-family:"Arvo",serif;font-weight:400;font-size:52px;color:var(--white);letter-spacing:1px}

  .slogan{position:absolute;left:312px;top:58px;font-family:"Arvo",serif;font-weight:700;font-size:36px;line-height:40px;color:var(--white)}

  .clouds{position:absolute;left:820px;top:0;width:380px;height:170px;
    background:radial-gradient(ellipse 55% 60% at 55% 45%,rgba(255,255,255,.95) 0,rgba(255,255,255,.85) 55%,rgba(255,255,255,0) 72%)}

  .main-nav{position:absolute;left:0;top:148px;display:flex;height:34px}
  .main-nav a{display:block;height:34px;padding:0 6px;font-family:"Arvo",serif;font-weight:700;font-size:20px;line-height:34px;color:var(--white);text-decoration:none;text-align:center;white-space:nowrap}
  .nav-home{width:96px;background:var(--tab-home)}
  .nav-grandpa{width:136px;background:var(--tab-grandpa)}
  .nav-about{width:128px;background:var(--tab-about)}
  .nav-careers{width:120px;background:var(--tab-careers)}
  .nav-news{width:80px;background:var(--tab-news)}
  .nav-contact{width:160px;background:var(--tab-contact)}
  .nav-shop{width:72px;background:var(--tab-shop)}

  .content-panel{position:absolute;left:16px;top:220px;width:878px;height:456px;background:var(--white);border-radius:12px;box-shadow:0 2px 8px rgba(40,90,140,.15)}
  .intro{position:absolute;left:6px;top:24px;width:380px;font-family:"Lora",serif;font-style:italic;font-size:14px;line-height:20px;color:var(--ink-soft);text-align:justify;hyphens:auto}
  .intro p{margin-bottom:20px}
  .intro p:last-child{margin-bottom:0}
  .intro .highlight{color:var(--accent-blue)}
  .share-row{position:absolute;left:246px;top:258px;width:130px;display:flex;justify-content:flex-end;gap:10px;font-family:"Arimo",sans-serif;font-size:10px;font-weight:700;color:var(--follow-blue)}
  .share-row span{display:flex;flex-direction:column;align-items:center;gap:2px}
  .share-row i{display:block;width:26px;height:26px;background:var(--follow-blue);border-radius:5px}
  .thumbs{position:absolute;left:132px;top:298px;display:flex;gap:22px}
  .thumb{width:66px;height:60px;border:1px solid #ddd}
  .thumb-a{background:linear-gradient(180deg,#f7b733,#7ec850)}
  .thumb-b{background:linear-gradient(180deg,#7a5230,#8cc65a)}
  .thumb-c{background:linear-gradient(180deg,#e9a04d,#6fbf4f)}
  .slider{position:absolute;left:400px;top:30px;width:460px;height:326px;background:linear-gradient(180deg,#5db6ee 0,#a6dcf6 40%,#79c25a 62%,#3f8f3a 100%)}
  .like-btn{position:absolute;left:814px;top:366px;width:44px;height:16px;border:1px solid #b9c4dc;background:#eef1f8;border-radius:2px;font-family:"Arimo",sans-serif;font-size:10px;line-height:14px;color:#3b5998;text-align:center}

  .leaf-panel{position:absolute;left:924px;top:208px;width:276px;height:468px;border-radius:0 0 0 180px;background:linear-gradient(170deg,var(--leaf-light) 0,var(--leaf-dark) 100%)}
  .side-box{position:absolute;left:970px;width:200px;background:var(--white);border-radius:12px;padding:8px 10px;overflow:hidden}
  .side-news{top:212px;height:204px}
  .side-gallery{top:432px;height:232px}
  .side-title{font-family:"Lora",serif;font-style:italic;font-weight:700;font-size:11px;line-height:13px;color:var(--ink)}
  .side-title span{font-weight:400}
  .side-body{margin-top:6px;font-family:"Arimo",sans-serif;font-size:10.5px;line-height:13px;color:#333}
  .side-photo{width:108px;height:84px;margin-top:6px;background:linear-gradient(160deg,#c7d9e8,#e6b89c)}

  .follow-band{position:absolute;left:0;top:676px;width:1200px;height:68px;background:linear-gradient(180deg,#d9effb,#eaf7fd)}
  .follow-label{position:absolute;left:40px;top:22px;font-family:"Lora",serif;font-weight:700;font-size:18px;color:var(--follow-blue)}
  .follow-links{position:absolute;left:172px;top:18px;display:flex;gap:22px}
  .follow-links span{display:flex;align-items:center;gap:6px;font-family:"Lora",serif;font-weight:700;font-size:16px;color:var(--follow-blue)}
  .follow-links i{display:block;width:30px;height:30px;border-radius:6px;background:var(--follow-blue)}

  .site-footer{position:absolute;left:0;top:744px;width:1200px;height:18px;background:var(--footer-brown);font-family:"Arimo",sans-serif;font-size:9px;line-height:18px;color:var(--white);text-align:center}
</style>
</head>
<body>
<div class="canvas">
  <div class="page">
    <div class="clouds" role="img" aria-label="Soft white clouds in the sky"></div>

    <header>
      <div class="brand"><span class="brand-dot"></span><span class="brand-name">Tovira</span></div>
      <h1 class="slogan">A new era of<br>children’s media</h1>
    </header>

    <nav class="main-nav">
      <a class="nav-home" href="#">HOME</a>
      <a class="nav-grandpa" href="#">GRANDPA</a>
      <a class="nav-about" href="#">ABOUT US</a>
      <a class="nav-careers" href="#">CAREERS</a>
      <a class="nav-news" href="#">NEWS</a>
      <a class="nav-contact" href="#">CONTACT US</a>
      <a class="nav-shop" href="#">SHOP</a>
    </nav>

    <main class="content-panel">
      <div class="intro" lang="en">
        <p>“Tovira means “<span class="highlight">butterfly</span>” in Korean. Just as a caterpillar transforms into a butterfly, Tovira Studios takes the reader on an unforgettable journey of metamorphosis through our stories.</p>
        <p>We turn children’s books into a high-quality interactive experience on mobile platforms – breathing magic back into books, and inspiring people to fall back in love with reading.</p>
        <p>Through our unique characters full of heart and spirit, our stories delight and inspire young and old alike.”</p>
      </div>
      <div class="share-row"><span><i></i>Chirpline</span><span><i></i>Facelinks</span></div>
      <div class="thumbs">
        <div class="thumb thumb-a" role="img" aria-label="Book screenshot thumbnail: sunny garden"></div>
        <div class="thumb thumb-b" role="img" aria-label="Book screenshot thumbnail: tree and swing"></div>
        <div class="thumb thumb-c" role="img" aria-label="Book screenshot thumbnail: story character"></div>
      </div>
      <div class="slider" role="img" aria-label="Illustrated book scene: a child on a trampoline in a sunny backyard with a tree, swing and doghouse"></div>
      <div class="like-btn">Like</div>
    </main>

    <div class="leaf-panel" role="img" aria-label="Large green leaf decoration"></div>
    <aside>
      <section class="side-box side-news">
        <h2 class="side-title">Section on Latest News with a few of the latest entries</h2>
        <p class="side-body">Lorem ipsum dolor sit amet, consectetur adipiscing elit. Proin mattis purus in risus ultrices sit amet interdum sem pellentesque. Duis vehicula, purus sit</p>
      </section>
      <section class="side-box side-gallery">
        <h2 class="side-title">Section on latest sister images &amp; comments that visitors <span>have posted, which takes you to the “Their Garden” page.</span></h2>
        <div class="side-photo" role="img" aria-label="Visitor-submitted photo"></div>
        <p class="side-body">Lorem ipsum dolor sit amet, consectetur adipiscing elit. Proin mattis purus in risus ultrices sit amet interdum sem pellentesque. Duis vehicula, purus sit</p>
      </section>
    </aside>

    <div class="follow-band">
      <span class="follow-label">follow us on</span>
      <div class="follow-links"><span><i></i>Facelinks</span><span><i></i>Chirpline</span></div>
    </div>
    <footer class="site-footer">lorem ipsum © sit dolor amet &nbsp;- 2011 - all right reserved</footer>
  </div>
</div>
</body>
</html>
```